Author needs book cover design for RC car book

Book Title: Complete Miniature Circuit Drivers Handbook
Author: Mark T Hollins (www.markthollins.example)
Front Cover size: 6” (152.4mm) wide x 9” (228.6mm) high

Cars: There will be 2 Radio Control (RC) cars on the cover [must be colour photos]:

• 1 x F1 car
• 1 x 1/12th scale car

You can use any real F1 car photo and any real QX7 car photo (for the 1/12th) or for the 1/12th you can google “12th scale pan car”. Once the design is nearly finalised we will provide photos of RC cars to be substituted in whatever orientation you have used. If specific colours are needed for the design then we can have car bodies painted and photographed for this purpose. For purposes of scale between the 2 cars, the F1 car is 420mm long and the 1/12th car is 320mm long.

Champions: There will be photos of 2 RC champions on the cover (Headshots, or head and shoulders). It is important that these are clearly visible as having them endorse the book is a major selling point. Details of these champions are to be confirmed, use placeholder images. One will have the title “1/12th Champion” and one will have the title “F1 Champion”. Additional text “With Pro Tips from GLOVTA World Champions”.

Background: up to the designer
Fonts: up to the designer
Colours: up to the designer

Book is 130 colour pages. Table of Contents attached.

Optional things that could be on the cover but that I’m not sure whether to include:

• Velbrook Pitline logo (www.velbrookpitline.example.au) – the #1 RC F1 website in the world, which I own
• An attention-grabbing hook or sub-heading such as “Ultimate Pan Car Performance” (or similar)

Rear cover: will definitely have Velbrook Pitline logo, the Pembury publishing logo and a white box where the bar code will go which is 1.75” wide by 1” high. Rear cover text:
“Your complete guide to 12th scale and F1 pan cars with everything you need to know; from basic setup how-to’s, to advanced techniques used by world champions. Everything you need to drive faster is in this book.

We provide you with the information you need to fast track your success, whether racing or bashing. Whether you’re a beginner or a pro driver, the setup advice, checklists, case studies and quick reference material are an essential addition to your pit table. Packed full of the information you need to give you the edge, in an easy to read format with examples.”

Completed image should show rear cover, spine and front cover. Background image might wrap around front and back or each may have a different background. Image will be used on printed book and ebook. Formats required: high quality image file(s), PDF and Adobe Illustrator. Files must be CMYK print ready at 300dpi or higher. Colour density must not exceed 300% and should ideally be around 240% if practical.

```html
<!DOCTYPE html>
<html lang="en">
<head>
<meta charset="utf-8">
<title>Complete Miniature Circuit Drivers Handbook – Cover Wrap</title>
<link rel="stylesheet" href="https://fonts.googleapis.com/css2?family=Anton&family=Open+Sans:wght@400;600&display=swap">
<style>
  :root {
    --stage: #d9d9d6;
    --yellow-front: #e8e84a;
    --yellow-back: #d6d826;
    --ink: #111111;
    --logo-grey: #555555;
    --check-dark: #2a2a2a;
    --check-light: #f2f2f2;
    --white: #ffffff;
  }
  * { box-sizing: border-box; margin: 0; padding: 0; }
  html, body { width: 1200px; height: 864px; overflow: hidden; background: var(--stage); }
  .wrap {
    position: absolute; left: 37px; top: 32px;
    width: 1126px; height: 800px;
    display: flex;
  }
  .panel { position: relative; height: 800px; overflow: hidden; }
  .back { width: 533px; background: var(--yellow-back); }
  .spine { width: 60px; background: var(--yellow-front); border-left: 1px solid rgba(0,0,0,.12); border-right: 1px solid rgba(0,0,0,.12); }
  .front { width: 533px; background: var(--yellow-front); }

  .checker {
    position: absolute;
    background: linear-gradient(135deg, var(--check-dark), var(--check-light) 50%, var(--check-dark));
  }
  .field { position: absolute; border-radius: 46px; }
  .back .field { background: var(--yellow-back); }
  .front .field { background: var(--yellow-front); }

  .brand {
    font-family: "Anton", sans-serif; color: var(--logo-grey);
    letter-spacing: .5px; display: flex; align-items: center; gap: 8px;
    position: absolute;
  }
  .brand .mark { width: 12px; height: 12px; background: var(--logo-grey); }

  .blurb {
    position: absolute; left: 70px; top: 250px; width: 393px;
    font-family: "Open Sans", sans-serif; font-size: 11.5px; line-height: 1.5;
    color: var(--ink); text-align: center;
  }
  .blurb p + p { margin-top: 10px; }
  .publisher {
    position: absolute; left: 0; width: 533px; top: 440px;
    font-family: "Anton", sans-serif; font-size: 20px; color: var(--ink);
    display: flex; align-items: center; justify-content: center; gap: 8px;
  }
  .publisher .mark { width: 14px; height: 14px; background: var(--ink); }
  .barcode-box {
    position: absolute; left: 166px; top: 575px; width: 200px; height: 115px;
    background: var(--white);
  }

  .spine-brand {
    left: 0; top: 36px; width: 60px; justify-content: center;
    font-size: 11px; line-height: 1.3; text-align: center;
  }
  .spine-title {
    position: absolute; left: 14px; top: 110px; height: 540px;
    writing-mode: vertical-rl;
    font-family: "Anton", sans-serif; font-size: 24px; color: var(--ink);
    letter-spacing: .5px; white-space: nowrap;
  }
  .spine-publisher { position: absolute; left: 22px; top: 690px; width: 16px; height: 16px; background: var(--ink); }

  .front-brand { left: 0; width: 533px; top: 34px; justify-content: center; font-size: 22px; }
  .track-line { position: absolute; left: 0; top: 0; }
  .title {
    position: absolute; left: 30px; top: 100px; width: 420px;
    font-family: "Anton", sans-serif; font-weight: 400; font-size: 38px; line-height: 1.08;
    color: var(--ink); text-transform: uppercase; text-align: center;
  }
  .placeholder { position: absolute; }
  .car-twelfth {
    left: 360px; top: 190px; width: 150px; height: 70px; border-radius: 30px 30px 8px 8px;
    background: linear-gradient(90deg, #1f2a6b, #c2182b 60%, #30344a);
  }
  .car-f1 {
    left: 150px; top: 290px; width: 330px; height: 140px; border-radius: 40px 60px 20px 20px;
    background: linear-gradient(100deg, #1a1a1a, #3b3b3b 45%, #b38a1f 80%, #1a1a1a);
  }
  .flag-small {
    left: 120px; top: 330px; width: 50px; height: 36px;
    background: linear-gradient(135deg, var(--check-dark), var(--check-light));
  }
  .champ-label {
    position: absolute; font-family: "Anton", sans-serif; font-size: 13px;
    color: var(--ink); text-transform: uppercase; text-align: center; width: 90px; line-height: 1.1;
  }
  .headshot {
    position: absolute; width: 86px; height: 86px; border-radius: 50%;
    border: 3px solid var(--white);
    background: radial-gradient(circle at 50% 40%, #c9a88c, #2b5aa8 75%);
  }
  .pro-tips {
    position: absolute; left: 225px; top: 630px; width: 280px;
    font-family: "Anton", sans-serif; font-size: 17px; line-height: 1.15;
    color: var(--ink); text-align: center; text-transform: uppercase;
  }
  .credits {
    position: absolute; left: 315px; top: 680px; width: 190px;
    font-family: "Open Sans", sans-serif; font-size: 9px; line-height: 1.35;
    color: var(--ink); text-align: center;
  }
</style>
</head>
<body>
<main class="wrap">

  <section class="panel back" aria-label="Rear cover">
    <div class="checker" role="img" aria-label="Chequered flag pattern" style="right:0; top:0; width:150px; height:130px;"></div>
    <div class="checker" role="img" aria-label="Chequered flag pattern" style="left:0; bottom:0; width:533px; height:120px;"></div>
    <div class="field" style="left:-40px; top:24px; width:547px; height:736px;"></div>

    <div class="brand" style="left:0; width:533px; top:170px; justify-content:center; font-size:30px;">
      <span class="mark"></span>Velbrook Pitline
    </div>

    <div class="blurb">
      <p>Your complete guide to 12th scale and F1 pan cars with everything you need to know; from basic setup how-to’s, to advanced techniques used by world champions. Everything you need to drive faster is in this book.</p>
      <p>We provide you with the information you need to fast track your success, whether racing or bashing. Whether you’re a beginner or a pro driver, the setup advice, checklists, case studies and quick reference material are an essential addition to your pit table. Packed full of the information you need to give you the edge, in an easy to read format with examples.</p>
    </div>

    <div class="publisher"><span class="mark"></span>Pembury</div>
    <div class="barcode-box"></div>
  </section>

  <section class="panel spine" aria-label="Spine">
    <div class="brand spine-brand">Velbrook<br>Pitline</div>
    <div class="spine-title">Complete Miniature Circuit Drivers Handbook</div>
    <div class="spine-publisher"></div>
  </section>

  <section class="panel front" aria-label="Front cover">
    <div class="checker" role="img" aria-label="Chequered flag pattern" style="right:0; top:0; width:150px; height:120px;"></div>
    <div class="checker" role="img" aria-label="Chequered flag pattern" style="left:0; bottom:0; width:533px; height:130px;"></div>
    <div class="field" style="left:-40px; top:22px; width:550px; height:700px;"></div>

    <svg class="track-line" width="533" height="800" viewBox="0 0 533 800" aria-hidden="true">
      <path d="M30 90 Q260 60 410 130 Q520 220 470 420 Q420 640 220 700" fill="none" stroke="var(--ink)" stroke-width="4"/>
    </svg>

    <div class="brand front-brand">Velbrook Pitline</div>

    <h1 class="title">Complete Miniature Circuit Drivers Handbook</h1>

    <div class="placeholder car-twelfth" role="img" aria-label="Photo of a 1/12th scale RC pan car"></div>
    <div class="placeholder flag-small" role="img" aria-label="Small chequered flag"></div>
    <div class="placeholder car-f1" role="img" aria-label="Photo of an F1 RC car"></div>

    <div class="champ-label" style="left:248px; top:500px;">1/12th<br>Champion</div>
    <div class="champ-label" style="left:358px; top:500px;">F1<br>Champion</div>
    <div class="headshot" role="img" aria-label="Headshot of the 1/12th champion" style="left:250px; top:534px;"></div>
    <div class="headshot" role="img" aria-label="Headshot of the F1 champion" style="left:360px; top:534px;"></div>

    <p class="pro-tips">With Pro Tips From GLOVTA<br>World Champions</p>

    <p class="credits">By Mark T Hollins<br>www.markthollins.example<br>www.velbrookpitline.example.au</p>
  </section>

</main>
</body>
</html>
```